" A Nimbo Cash é uma lean startup que tem como objetivo conscientizar e ensinar as pessoas como lidar com o dinheiro de forma inteligente e segura, através de cursos que englobam desde conceitos de modelo mental (mindset) até noções básicas de investimento no caixa lume. A ideia é realmente associar a administração do dinheiro a algo que não precisa ser estressante e desgastante, por isso a paleta de cores mais frias. (vide anexo) O negócio é dividido em duas frentes, um com foco B2B e outro com foco B2C, e o público alvo são pessoas economicamente ativas. "

```html
<!DOCTYPE html>
<html lang="pt-BR">
<head>
<meta charset="UTF-8">
<title>Nimbo Cash — Pasta e Papel Timbrado</title>
<link rel="stylesheet" href="https://fonts.googleapis.com/css2?family=Roboto+Condensed:wght@400;700&display=swap">
<style>
  :root {
    --canvas: #ffffff;
    --stage: #c9c9c9;
    --ink-black: #000000;
    --paper: #ffffff;
    --brand-green: #6dbb3c;
    --band-mid: #5a5a5a;
    --band-dark: #3a3a3a;
    --text-light: #ffffff;
    --text-dark: #3b3b3b;
    --muted-light: #bdbdbd;
    --watermark: #ececec;
  }
  * { margin: 0; padding: 0; box-sizing: border-box; }
  html, body {
    width: 1200px; height: 1200px; overflow: hidden;
    background: var(--canvas);
    font-family: "Roboto Condensed", Arial, sans-serif;
  }
  .stage {
    position: absolute; left: 36px; top: 216px;
    width: 1128px; height: 756px;
    background: var(--stage);
  }
  .sheet {
    position: absolute; top: 55px;
    width: 478px; height: 677px;
  }
  .folder-cover { left: 58px; background: var(--ink-black); }
  .letterhead { left: 564px; background: var(--paper); overflow: hidden; }

  .brand { display: flex; align-items: center; gap: 10px; }
  .brand-mark { width: 22px; height: 22px; background: var(--brand-green); flex: none; }
  .brand-name { font-weight: 700; line-height: 1; white-space: nowrap; }

  .folder-cover .brand-block {
    position: absolute; left: 0; right: 0; top: 300px;
    display: flex; flex-direction: column; align-items: center;
  }
  .folder-cover .brand-name { font-size: 52px; color: var(--text-light); }
  .folder-cover .brand-mark { width: 28px; height: 28px; }
  .tagline {
    margin-top: 6px; font-size: 18px; letter-spacing: 7px;
    color: var(--muted-light); font-weight: 400; text-transform: uppercase;
  }
  .contact {
    position: absolute; left: 0; right: 0; top: 580px;
    text-align: center; color: var(--muted-light);
    font-size: 10px; line-height: 1.45;
  }

  .watermark {
    position: absolute; left: 150px; top: 105px;
    width: 300px; height: 300px; background: var(--watermark);
  }
  .letterhead .brand-block { position: absolute; left: 64px; top: 565px; }
  .letterhead .brand-name { font-size: 30px; color: var(--text-dark); }
  .letterhead .tagline { font-size: 9px; letter-spacing: 3.5px; margin-top: 3px; color: #9a9a9a; }

  .footer-bands { position: absolute; left: 0; right: 0; top: 648px; height: 12px; display: flex; }
  .band-green { flex: 336; background: var(--brand-green); }
  .band-mid { flex: 72; background: var(--band-mid); }
  .band-dark { flex: 70; background: var(--band-dark); }
</style>
</head>
<body>
  <main class="stage">
    <section class="sheet folder-cover">
      <div class="brand-block">
        <div class="brand">
          <span class="brand-mark"></span>
          <span class="brand-name">Nimbo Cash</span>
        </div>
        <div class="tagline">Finanças Pessoais</div>
      </div>
      <address class="contact" style="font-style:normal">
        Rua Endereço Completo<br>
        Bairro · Centro · Cidade/UF<br>
        Telefone (11) 0000-0000
      </address>
    </section>

    <section class="sheet letterhead">
      <div class="watermark" aria-hidden="true"></div>
      <div class="brand-block">
        <div class="brand">
          <span class="brand-mark" style="width:16px;height:16px"></span>
          <span class="brand-name">Nimbo Cash</span>
        </div>
        <div class="tagline">Finanças Pessoais</div>
      </div>
      <div class="footer-bands">
        <span class="band-green"></span>
        <span class="band-mid"></span>
        <span class="band-dark"></span>
      </div>
    </section>
  </main>
</body>
</html>
```